Business Card Design

Business card design.

Business card is to have logo, website address and email address.

Website is www.brightkettle.ie
Email is info@brightkettle.ie

I have ordered Business Card Printing via Print Harbor, the Double-sided colour printed option with gloss finish.

Industry/Entity Type

Business

```html
<!DOCTYPE html>
<html lang="en">
<head>
<meta charset="utf-8">
<title>Bright Kettle – Business Card</title>
<link rel="stylesheet" href="https://fonts.googleapis.com/css2?family=Archivo:wght@800&family=EB+Garamond:wght@500;600&display=swap">
<style>
  :root {
    --backdrop: #e9e6e2;
    --card-white: #ffffff;
    --card-dark: #252424;
    --brand-red: #b3191c;
    --brand-red-deep: #8f1214;
    --label-rust: #b5562f;
    --ink: #161616;
    --text-light: #f4f1ec;
  }
  html, body {
    margin: 0;
    padding: 0;
    width: 1200px;
    height: 1000px;
    overflow: hidden;
    background: var(--backdrop);
  }
  .canvas {
    position: relative;
    width: 1200px;
    height: 1000px;
  }
  .card {
    position: absolute;
    left: 310px;
    width: 580px;
    height: 332px;
    box-shadow: 0 10px 26px rgba(0,0,0,0.22);
  }
  .card--front { top: 110px; }
  .card--back  { top: 558px; }
  .card svg { display: block; width: 100%; height: 100%; }
  .brand-name {
    font-family: "Archivo", "Arial Black", sans-serif;
    font-weight: 800;
    fill: var(--ink);
    letter-spacing: 0.5px;
  }
  .web-address {
    font-family: "EB Garamond", Georgia, serif;
    font-weight: 600;
    fill: var(--text-light);
  }
  .contact-label {
    font-family: "EB Garamond", Georgia, serif;
    font-weight: 600;
    fill: var(--label-rust);
  }
  .contact-value {
    font-family: "EB Garamond", Georgia, serif;
    font-weight: 500;
    fill: var(--text-light);
  }
</style>
</head>
<body>
<main class="canvas">

  <section class="card card--front" aria-label="Business card front">
    <svg viewBox="0 0 580 332" xmlns="http://www.w3.org/2000/svg">
      <rect class="card-base" width="580" height="332" fill="var(--card-white)"/>
      <path class="curve-band" d="M0 262 C 150 200, 360 120, 580 96 L580 332 L0 332 Z" fill="var(--brand-red)"/>
      <path class="curve-panel" d="M0 280 C 150 218, 360 138, 580 112 L580 332 L0 332 Z" fill="var(--card-dark)"/>
      <g class="brand-lockup">
        <circle cx="128" cy="66" r="14" fill="var(--brand-red)"/>
        <text class="brand-name" x="152" y="78" font-size="32" textLength="320" lengthAdjust="spacingAndGlyphs">BRIGHTKETTLE.IE</text>
      </g>
      <text class="web-address" x="300" y="258" font-size="40" text-anchor="middle">www.brightkettle.ie</text>
    </svg>
  </section>

  <section class="card card--back" aria-label="Business card back">
    <svg viewBox="0 0 580 332" xmlns="http://www.w3.org/2000/svg">
      <rect class="card-frame" width="580" height="332" fill="var(--brand-red)"/>
      <rect class="card-inner" x="24" y="24" width="532" height="284" fill="var(--card-white)"/>
      <path class="curve-band" d="M24 176 C 170 150, 330 230, 556 296 L556 308 L24 308 Z" fill="var(--brand-red-deep)"/>
      <path class="curve-panel" d="M24 192 C 160 168, 330 246, 556 310 L556 308 L24 308 Z" fill="var(--card-dark)"/>
      <g class="brand-lockup">
        <circle cx="196" cy="80" r="13" fill="var(--brand-red)"/>
        <text class="brand-name" x="218" y="91" font-size="29" textLength="300" lengthAdjust="spacingAndGlyphs">BRIGHTKETTLE.IE</text>
      </g>
      <g class="contact-details">
        <text x="52" y="246" font-size="22"><tspan class="contact-label">W:</tspan><tspan class="contact-value" dx="8">www.brightkettle.ie</tspan></text>
        <text x="52" y="278" font-size="22"><tspan class="contact-label">E:</tspan><tspan class="contact-value" dx="12">info@brightkettle.ie</tspan></text>
      </g>
    </svg>
  </section>

</main>
</body>
</html>
```